New Zealand Export company needs business cards

We need new business cards to match our new logo for a company based in New Zealand who deal specifically with the Pacific Islands. We source, consolidate and ship products out of New Zealand to the Pacific Islands. Will attach our old ones and also new logo.
Would like the Islands we deal with and the areas of work we have access to, to be included on the business cards.

Contact Information for Business Card

T +64 9 571 3048
F +64 9 571 6285
12-18 Kowhai Lane, Drury, 2113
PO Box 814, Drury, Auckland 2247, New Zealand
www.falconfreight.example.nz
E sales@falconfreight.example.nz

Font styles to use
Sans Serif

Colors
85abd2
33a6d7
ffffff

Requirements
Must have
• A company of PWM

```html
<!DOCTYPE html>
<html lang="en">
<head>
<meta charset="utf-8">
<title>Falcon Freight Business Card</title>
<link href="https://fonts.googleapis.com/css2?family=Poppins:wght@400;500;600&display=swap" rel="stylesheet">
<style>
  :root {
    --navy: #0d5aa7;
    --sky: #35b7e8;
    --ink: #4a4a4a;
    --rule: #8a8a8a;
    --paper: #ffffff;
    --paper-soft: rgba(255,255,255,0.82);
    --backdrop: #e4e4e4;
    --back-top: #1467ae;
    --back-bottom: #0b569f;
  }
  * { margin: 0; padding: 0; box-sizing: border-box; }
  html, body { width: 1200px; height: 1200px; overflow: hidden; }
  body {
    background: var(--backdrop);
    font-family: "Poppins", sans-serif;
    position: relative;
  }
  .card {
    position: absolute;
    left: 262px;
    width: 686px;
    height: 392px;
    overflow: hidden;
  }
  .card-front { top: 165px; background: var(--paper); }
  .card-back {
    top: 653px;
    background: linear-gradient(180deg, var(--back-top), var(--back-bottom));
  }

  .brand {
    position: absolute;
    right: 44px;
    top: 58px;
    display: flex;
    align-items: center;
    gap: 12px;
    color: var(--navy);
    font-weight: 600;
    font-size: 30px;
    letter-spacing: 1px;
  }
  .brand-square { width: 22px; height: 22px; background: var(--navy); }

  .person { position: absolute; left: 38px; top: 208px; }
  .person-name { color: var(--navy); font-weight: 500; font-size: 22px; line-height: 1.1; }
  .person-title { color: var(--sky); font-size: 16px; line-height: 1.4; }

  .divider {
    position: absolute; left: 38px; right: 44px; top: 266px;
    height: 1px; background: var(--rule);
  }

  .contacts {
    position: absolute; left: 38px; top: 276px;
    list-style: none; color: var(--ink); font-size: 15.5px; line-height: 20px;
  }
  .contacts li { display: flex; align-items: center; gap: 10px; }
  .contacts svg { width: 14px; height: 14px; fill: var(--navy); }

  .address {
    position: absolute; right: 44px; top: 293px;
    text-align: right; color: var(--ink); font-size: 15.5px; line-height: 19.5px;
    font-style: normal;
  }

  .band { position: absolute; left: 0; right: 0; bottom: 0; height: 14px; }

  .back-brand {
    position: absolute; left: 0; right: 0; top: 120px;
    display: flex; justify-content: center; align-items: center; gap: 16px;
    color: var(--paper); font-weight: 600; font-size: 44px; letter-spacing: 2px;
  }
  .back-brand .brand-square { background: var(--paper); width: 30px; height: 30px; }

  .services {
    position: absolute; left: 0; right: 0; top: 200px;
    text-align: center; color: var(--paper); font-size: 15px; font-weight: 500;
    letter-spacing: 1.5px; text-transform: uppercase;
  }
  .islands {
    position: absolute; left: 40px; right: 40px; top: 236px;
    text-align: center; color: var(--paper-soft); font-size: 13.5px; line-height: 20px;
  }
  .back-url {
    position: absolute; left: 0; right: 0; top: 338px;
    text-align: center; color: var(--paper); font-size: 15.5px; letter-spacing: 2px;
  }
</style>
</head>
<body>
  <section class="card card-front">
    <div class="brand"><span class="brand-square"></span>FALCON FREIGHT</div>

    <div class="person">
      <p class="person-name">TESSA LANG</p>
      <p class="person-title">Sales Manager</p>
    </div>

    <div class="divider"></div>

    <ul class="contacts">
      <li><svg viewBox="0 0 16 16"><path d="M3.5 1l2.5 3-1.5 1.8c.8 1.8 2 3 3.8 3.8L10 8l3 2.5-1.2 2.5C7 13 3 9 2.2 3z"/></svg>+64 9 571 3048</li>
      <li><svg viewBox="0 0 16 16"><rect x="4" y="1" width="8" height="4"/><rect x="1" y="6" width="14" height="6" rx="1"/><rect x="4" y="10" width="8" height="5" fill="#fff" stroke="#0d5aa7"/></svg>+64 9 571 6285</li>
      <li><svg viewBox="0 0 16 16"><rect x="1" y="3" width="14" height="10"/><path d="M1 3l7 6 7-6" fill="none" stroke="#fff" stroke-width="1.5"/></svg>sales@falconfreight.example.nz</li>
      <li><svg viewBox="0 0 16 16"><circle cx="8" cy="8" r="7"/><path d="M5 4c2 1 1 3 3 3s1 3 0 5M10 3c0 2 2 2 3 3" fill="none" stroke="#fff" stroke-width="1.3"/></svg>www.falconfreight.example.nz</li>
    </ul>

    <address class="address">
      12-18 Kowhai Lane, Drury, 2113<br>
      PO Box 814, Drury<br>
      Auckland 2247, New Zealand
    </address>

    <svg class="band" viewBox="0 0 686 14" preserveAspectRatio="none">
      <polygon points="0,0 398,0 394,14 0,14" fill="var(--navy)"/>
      <polygon points="404,0 686,0 686,14 400,14" fill="var(--sky)"/>
    </svg>
  </section>

  <section class="card card-back">
    <div class="back-brand"><span class="brand-square"></span>FALCON FREIGHT</div>
    <p class="services">Sourcing &nbsp;|&nbsp; Consolidation &nbsp;|&nbsp; Shipping</p>
    <p class="islands">Samoa · Tonga · Fiji · Cook Islands · Niue · Vanuatu<br>Tokelau · Tuvalu · Kiribati · Solomon Islands</p>
    <p class="back-url">www.falconfreight.example.nz</p>
  </section>
</body>
</html>
```